Product Design for BelNova

Design Brief for BelNova Product Packaging

Objective:
Create a cohesive, elegant, and brand-consistent packaging design for the BelNova product line. The signature visual theme should reflect luxury, femininity, and clean beauty values.

---

🎨 Core Design Direction

Unified Aesthetic: All containers must prominently feature the floral pattern shown in "Pattern Reference: Image 3". This design serves as the brand's signature aesthetic and must be applied uniformly across all SKUs.

Brand Logo Placement: The BelNova logo (provided) should be clearly visible and harmoniously integrated into the patterned background.

Color Palette: Base colors should complement the brand’s primary palette: black, blush pink, and white.

---

🧴 Product-Specific Packaging Specifications

1. Mascara

Bottle Type: Sleek mascara tube with a wand applicator

Capacity: 5ml

Design: Use floral pattern from Pattern Reference Image 3. Ensure the pattern does not obstruct the readability of the logo or any regulatory text.

2. Eyebrow Growth Serum

Bottle Type: 5ml tube with fine-tip brush applicator

Capacity: 5ml

Design: Same floral pattern, scaled and applied proportionally to match the mascara for consistency

3. Eyelash Growth Serum

Bottle Type: 5ml tube with fine-tip brush (similar to the eyebrow serum, unless otherwise advised)

Capacity: 5ml

Design: Identical styling to maintain unity across lash & brow products

4. Anti-Aging Serum or Lotion

Bottle Type: 30ml airless pump bottle (preferred for hygiene and product stability)

Capacity: 30ml

Design: Apply floral pattern from Pattern Reference and scale appropriately for larger surface area

5. Hair Growth Spray

Bottle Type: 50ml fine mist spray bottle

Capacity: 50ml

Design: Pattern applied and scaled for taller profile; maintain visual harmony with skincare line

---

📦 Additional Notes

Please ensure packaging aligns with clean beauty standards (no overly glossy plastic finishes, avoid excessive secondary packaging unless sustainable).

Materials should be eco-conscious where possible.

If embossing, foil stamping, or UV finishing is available for logo accents, please suggest options.

```html
<!DOCTYPE html>
<html lang="en">
<head>
<meta charset="utf-8">
<title>BelNova Packaging Line</title>
<link rel="stylesheet" href="https://fonts.googleapis.com/css2?family=Playfair+Display:wght@400;700&display=swap">
<style>
  :root {
    --teal: #2e7774;
    --label-light: #f9e9e0;
    --label-mid: #f6d9cc;
    --label-deep: #f1c7b8;
    --amber: #6b2f12;
    --amber-light: #9a4a22;
    --black: #1c1c1e;
    --cap-pink: #f3cdbd;
    --silver: #9c9a98;
    --white: #fbfbfa;
    --bg-one: #f4e6df;
    --bg-two: #efefee;
    --bg-three: #e7e7e8;
    --bg-four: #e8d5ca;
  }
  * { margin: 0; padding: 0; box-sizing: border-box; }
  html, body { width: 1200px; height: 3432px; overflow: hidden; }
  body { position: relative; font-family: "Playfair Display", Georgia, serif; color: var(--teal); }

  .panel { position: absolute; left: 0; width: 1200px; overflow: hidden; }
  .panel-serum { top: 0; height: 800px; background: var(--bg-one); }
  .panel-spray { top: 800px; height: 860px; background: var(--bg-two); }
  .panel-mascara { top: 1660px; height: 826px; background: var(--bg-three); }
  .panel-pump { top: 2486px; height: 946px; background: var(--bg-four); }

  .container-art { position: absolute; left: 0; top: 0; }

  .label { position: absolute; overflow: hidden; }
  .pattern-fill {
    position: absolute; inset: 0;
    background: linear-gradient(155deg, var(--label-light) 0%, var(--label-mid) 55%, var(--label-deep) 100%);
  }
  .label-content {
    position: absolute; inset: 0;
    display: flex; flex-direction: column; align-items: center; justify-content: center;
    text-align: center;
  }
  .brand { font-weight: 400; line-height: 1; white-space: nowrap; }
  .product { font-weight: 700; line-height: 1.15; }
  .volume { font-weight: 700; line-height: 1; }

  /* dropper serum */
  .serum-bottle {
    position: absolute; left: 463px; top: 90px; width: 260px; height: 720px;
    transform: rotate(24deg); transform-origin: 50% 55%;
  }
  .label-serum { left: 5px; top: 320px; width: 250px; height: 330px; }
  .label-serum .brand { font-size: 40px; margin-bottom: 34px; }
  .label-serum .product { font-size: 27px; margin-bottom: 46px; }
  .label-serum .volume { font-size: 26px; }

  /* spray bottle */
  .label-spray { left: 490px; top: 426px; width: 212px; height: 260px; border-radius: 4px; }
  .label-spray .brand { font-size: 30px; margin-bottom: 28px; }
  .label-spray .product { font-size: 16px; margin-bottom: 40px; }
  .label-spray .volume { font-size: 14px; }

  /* mascara tube */
  .label-mascara {
    left: 180px; top: 450px; width: 683px; height: 204px;
    border-radius: 10px 4px 4px 10px;
    clip-path: polygon(0 5%, 100% 0, 100% 100%, 0 95%);
  }
  .label-mascara .volume {
    position: absolute; left: 34px; top: 50%; transform: translateY(-50%);
    writing-mode: vertical-rl; font-size: 26px;
  }
  .label-mascara .brand {
    position: absolute; left: 146px; top: 50%; transform: translateY(-50%);
    font-size: 92px;
  }

  /* pump bottle and jar lid */
  .label-pump { left: 500px; top: 245px; width: 166px; height: 637px; border-radius: 3px; }
  .label-pump .brand-vertical {
    position: absolute; left: 50%; top: 300px;
    transform: translate(-50%, -50%) rotate(-90deg);
    font-size: 64px;
  }
  .label-pump .volume { position: absolute; bottom: 40px; left: 0; right: 0; text-align: center; font-size: 22px; }

  .label-lid { left: 605px; top: 555px; width: 300px; height: 300px; border-radius: 50%; box-shadow: 0 6px 18px rgba(120, 80, 60, .18); }
  .label-lid .brand { font-size: 38px; }
</style>
</head>
<body>
  <section class="panel panel-serum">
    <div class="serum-bottle">
      <svg class="container-art" width="260" height="720" viewBox="0 0 260 720" aria-hidden="true">
        <rect x="100" y="0" width="60" height="130" rx="28" fill="var(--black)"/>
        <rect x="72" y="120" width="116" height="110" rx="8" fill="var(--black)"/>
        <rect x="90" y="228" width="80" height="34" fill="var(--amber)"/>
        <path d="M90 262 C 20 280 0 300 0 340 L0 690 Q0 710 20 710 L240 710 Q260 710 260 690 L260 340 C 260 300 240 280 170 262 Z" fill="var(--amber)"/>
        <rect x="18" y="300" width="14" height="380" rx="7" fill="var(--amber-light)" opacity=".5"/>
      </svg>
      <div class="label label-serum">
        <div class="pattern-fill" role="img" aria-label="Blush watercolour floral pattern"></div>
        <div class="label-content">
          <p class="brand">BelNova</p>
          <p class="product">Anti-Aging<br>Serum</p>
          <p class="volume">30ml</p>
        </div>
      </div>
    </div>
  </section>

  <section class="panel panel-spray">
    <svg class="container-art" width="1200" height="860" viewBox="0 0 1200 860" aria-hidden="true">
      <rect x="546" y="90" width="104" height="140" rx="18" fill="#dfe2e6" opacity=".7" stroke="#c9ccd1" stroke-width="2"/>
      <rect x="574" y="118" width="22" height="26" rx="4" fill="var(--black)"/>
      <rect x="584" y="140" width="28" height="90" fill="var(--black)"/>
      <rect x="537" y="226" width="124" height="96" rx="6" fill="var(--black)"/>
      <path d="M560 320 C 500 330 489 360 489 400 L489 676 Q489 690 503 690 L688 690 Q702 690 702 676 L702 400 C 702 360 690 330 638 320 Z" fill="var(--amber)"/>
      <rect x="498" y="360" width="12" height="300" rx="6" fill="var(--amber-light)" opacity=".5"/>
    </svg>
    <div class="label label-spray">
      <div class="pattern-fill" role="img" aria-label="Blush watercolour floral pattern"></div>
      <div class="label-content">
        <p class="brand">BelNova</p>
        <p class="product">Hair Growth<br>Spray</p>
        <p class="volume">50ml</p>
      </div>
    </div>
  </section>

  <section class="panel panel-mascara">
    <svg class="container-art" width="1200" height="826" viewBox="0 0 1200 826" aria-hidden="true">
      <path d="M195 214 L600 194 Q609 194 609 203 L609 388 Q609 398 600 398 L195 380 Q187 380 187 370 L187 224 Q187 214 195 214 Z" fill="var(--cap-pink)"/>
      <rect x="609" y="288" width="372" height="14" rx="7" fill="var(--black)"/>
      <path d="M979 270 L1195 276 L1195 312 L979 318 Z" fill="var(--black)"/>
      <rect x="860" y="495" width="92" height="110" rx="8" fill="var(--black)"/>
    </svg>
    <div class="label label-mascara">
      <div class="pattern-fill" role="img" aria-label="Blush watercolour floral pattern"></div>
      <p class="volume">5ml</p>
      <p class="brand">BelNova</p>
    </div>
  </section>

  <section class="panel panel-pump">
    <svg class="container-art" width="1200" height="946" viewBox="0 0 1200 946" aria-hidden="true">
      <path d="M530 84 L690 84 Q712 86 713 104 L690 104 L640 104 L640 163 L560 163 L560 104 L530 104 Z" fill="var(--white)" stroke="#d8d2ce" stroke-width="2"/>
      <rect x="533" y="160" width="107" height="88" rx="4" fill="var(--silver)"/>
      <rect x="548" y="160" width="18" height="88" fill="#c9c7c5"/>
    </svg>
    <div class="label label-pump">
      <div class="pattern-fill" role="img" aria-label="Blush watercolour floral pattern"></div>
      <p class="brand brand-vertical">BelNova</p>
      <p class="volume">30ml</p>
    </div>
    <div class="label label-lid">
      <div class="pattern-fill" role="img" aria-label="Blush watercolour floral pattern"></div>
      <div class="label-content">
        <p class="brand">BelNova</p>
      </div>
    </div>
  </section>
</body>
</html>
```